CrashPals Personal Injury Lawyers Website (Wordpress)

We need a brand new website for our firm's new rebranding. The name of the website is www.crashpals-example.com. Our new brand will be a group of personal injury lawyers focused on representing only victims in car wrecks. We will be distinguishing ourselves from other law firms due to the fact that other law firms represent clients involving all forms of personal injury. We will only focus on car wrecks and this needs to be reflected on the website.

I have attached the new firm logo and stationary to show the designers the kind of look we are going for in the new website. It needs to be clean, pure, and show the potential clients that we only do one thing and we do it well. That thing is car wrecks.

Some examples of websites that we like are the following:
www.qtr-example.lu - nice interface and colors. nice navigation, we really like the biography pages for the individuals attorneys
www.harlowpinelegal-example.com - good layout, good navigation
www.maddoxtrevane-example.com - navigation bar follows the user whether the user goes up or down

We would like five separate pages -- (1) Home, (2) Client Resources, (3) Expertise / Car Wrecks, (4) Contact Us, (5) News

The Home page will be used for driving traffic and should have a call to action on the right at the top stating that we will send an ebook to anyone who gives their contact information. The ebook will explain how car wrecks work. This should also have room for youtube videos which will be added later.

The client resources will include blogs, books, and information for potential clients. It should be presented in a well developed manner which is both appealing to potential and current clients.

The expertise page will show that we only focus on car wrecks. This needs to be a recurrent theme throughout the entire website. This page will focus on car wrecks and the different aspects including damages, insurance, and investigation.

The Contact Us page will show a google map to our address and phone number. Please use generic information and we will fill in the gaps upon the selection.

News: the news page will show different articles related to past and present cases and the successes of those clients.

The overall page should be elegant and creative. Do not include courthouses, gavels or anything else related to the law. If you include these things, your design will automatically be excluded.
Updates

Please take note this design is now guaranteed. I look forward to receiving everyone's wonderful designs.

Target Market(s)

Persons involved in car wrecks

Industry/Entity Type

Legal

Coding

Coded - Design and coding required

Number of Pages Required

5+ page

Font styles to use
Serif
Sans Serif

Colors
ec1f27
ffffff
000000

Requirements
Must have
• Five pages which focus on representation of car wreck victims. The site must be clean and easy to navigate.
Nice to have
• Navigation bar should follow user up and down the page.
Should not have
• Gavels, court houses, anything related to the law. If your design has these aspects, it will automatically be rejected

```html
<!DOCTYPE html>
<html lang="en">
<head>
<meta charset="utf-8">
<title>CrashPals – Personal Injury Lawyers</title>
<link href="https://fonts.googleapis.com/css2?family=Roboto+Slab:wght@300;400;700&family=Open+Sans:wght@400;600;700&display=swap" rel="stylesheet">
<style>
:root{
  --red:#ec1f27;
  --black:#000;
  --ink:#222;
  --text:#666;
  --muted:#999;
  --white:#fff;
  --dark:#1d1d1d;
  --darker:#111;
  --light:#efefef;
  --line:#dcdcdc;
}
*{box-sizing:border-box;margin:0;padding:0}
html,body{width:1200px;height:3492px;overflow:hidden}
body{font-family:"Open Sans",Arial,sans-serif;color:var(--text);background:var(--white);font-size:13px;line-height:1.6}
.page{position:relative;width:1200px;height:3492px;overflow:hidden}
section,header,footer{position:relative;width:1200px}

/* header */
.site-header{height:80px;background:var(--white)}
.brand{position:absolute;left:180px;top:16px;display:flex;align-items:center;gap:10px}
.brand-mark{width:14px;height:14px;background:var(--red)}
.brand-name{font-family:"Open Sans",Arial,sans-serif;font-weight:600;font-size:26px;color:var(--ink);line-height:1}
.brand-tag{position:absolute;left:180px;top:50px;font-size:10px;color:var(--muted)}
.ebook-btn{position:absolute;left:868px;top:8px;width:150px;height:22px;background:var(--red);color:var(--white);font-size:9px;font-weight:700;letter-spacing:1px;display:flex;align-items:center;justify-content:center}
.main-nav{position:absolute;right:180px;top:46px;display:flex;align-items:center;gap:24px}
.main-nav a{font-size:10px;font-weight:700;color:var(--ink);text-decoration:none;letter-spacing:.5px}
.search-btn{width:26px;height:26px;background:var(--black);display:flex;align-items:center;justify-content:center}

/* hero */
.hero{height:420px;background:linear-gradient(180deg,#cfd6d9 0%,#9aa4ab 45%,#6c7479 70%,#b7b9ba 100%)}
.hero-media{position:absolute;inset:0}
.hero-caption{position:absolute;left:430px;top:316px;width:340px;background:rgba(0,0,0,.8);color:var(--white);text-align:center;padding:10px 16px 12px;font-family:"Roboto Slab",Georgia,serif;font-size:12px;font-weight:700;letter-spacing:.5px;line-height:1.5;border-bottom:3px solid var(--red)}
.hero-caption em{font-style:normal;color:var(--red)}

/* shared headings */
.section-title{font-family:"Roboto Slab",Georgia,serif;font-weight:400;font-size:32px;color:var(--ink);text-align:center;letter-spacing:1px}
.section-rule{width:60px;height:2px;background:var(--red);margin:10px auto 16px}
.section-lead{text-align:center;width:620px;margin:0 auto;font-size:12px;color:var(--muted)}

.about{height:180px;padding-top:36px}

/* evaluation band */
.evaluation{height:330px;background:linear-gradient(90deg,#151515,#2b2b2b 50%,#1a1a1a)}
.slide{position:absolute;left:260px;top:40px;width:440px;height:220px;background:linear-gradient(135deg,#5c0f12,#a5262b 45%,#6b6f73 80%,#3b3e41)}
.slide-dots{position:absolute;left:448px;top:272px;display:flex;gap:8px}
.slide-dots span{width:8px;height:8px;border-radius:50%;background:#777}
.slide-dots span:first-child{background:var(--white)}
.eval-form{position:absolute;left:850px;top:36px;width:190px}
.eval-form h3{font-family:"Roboto Slab",Georgia,serif;color:var(--white);font-size:14px;font-weight:400;letter-spacing:1px;margin-bottom:12px}
.field{height:24px;background:#2d2d2d;border:1px solid #444;margin-bottom:8px;color:#8a8a8a;font-size:10px;padding:4px 8px;line-height:1.4}
.field.tall{height:52px}
.btn-red{background:var(--red);color:var(--white);font-size:10px;font-weight:700;letter-spacing:1px;display:inline-flex;align-items:center;justify-content:center}
.eval-form .btn-red{width:74px;height:26px;float:right}

/* team */
.team{height:490px;padding-top:56px}
.team-arrows{position:absolute;left:966px;top:166px;display:flex;gap:4px}
.team-arrows span{width:18px;height:18px;background:var(--red);display:flex;align-items:center;justify-content:center}
.team-grid{position:absolute;left:192px;top:190px;display:flex;gap:24px}
.lawyer{width:120px}
.lawyer-photo{width:120px;height:150px;background:linear-gradient(180deg,#d8d8d8,#8e8e8e 60%,#3a3a3a)}
.lawyer-name{font-size:12px;font-weight:600;color:var(--ink);margin-top:10px;line-height:1.3}
.lawyer-role{font-size:9px;color:var(--red)}
.lawyer-meta{font-size:9px;color:var(--muted);line-height:1.4}
.lawyer-link{font-size:9px;color:var(--ink);font-weight:700}

/* video band */
.video-band{height:260px;background:#141414}
.video{position:absolute;left:240px;top:20px;width:480px;height:220px;background:linear-gradient(180deg,#8a9aa6,#5a5f63 55%,#2e2e2e)}
.video-bar{position:absolute;left:0;right:0;bottom:0;height:18px;background:rgba(0,0,0,.7)}
.video-bar i{position:absolute;left:10px;top:8px;width:300px;height:2px;background:var(--red)}
.video-title{position:absolute;left:8px;top:4px;color:var(--white);font-size:10px}
.play{position:absolute;left:210px;top:82px}
.video-copy{position:absolute;left:760px;top:30px;width:220px;color:#bbb}
.video-copy h3{font-family:"Roboto Slab",Georgia,serif;font-weight:400;color:var(--white);font-size:24px;margin-bottom:10px}
.video-copy p{font-size:11px;margin-bottom:16px}
.video-copy .btn-red{width:82px;height:26px}

/* blog */
.blog{height:600px;background:var(--light);padding-top:90px}
.blog-grid{position:absolute;left:168px;top:258px;display:flex;gap:24px}
.post{width:272px}
.post-image{height:180px}
.post h4{font-size:10px;font-weight:700;color:var(--ink);margin-top:16px;line-height:1.4;letter-spacing:.3px}
.post .meta{font-size:9px;color:var(--red);margin:4px 0}
.post p{font-size:10px;color:var(--muted);line-height:1.5}

/* touch + map */
.touch{height:130px;padding-top:52px}
.map{height:420px;background:linear-gradient(160deg,#3e3e3e,#2a2a2a 50%,#333)}
.map-zoom{position:absolute;left:14px;top:14px;width:22px}
.map-zoom span{display:flex;width:22px;height:22px;background:#555;color:var(--white);align-items:center;justify-content:center;font-size:14px;margin-bottom:2px}
.pin{position:absolute;left:590px;top:196px}

/* contact */
.contact{height:330px}
.contact h5{font-size:10px;font-weight:700;color:var(--ink);letter-spacing:1px;border-bottom:1px solid var(--line);padding-bottom:6px;margin-bottom:10px}
.contact-left{position:absolute;left:170px;top:22px;width:196px}
.contact-left label,.contact-right label{font-size:9px;color:var(--muted);display:block;margin-bottom:3px}
.input{height:22px;border:1px solid var(--line);background:var(--white);margin-bottom:10px}
.input.grey{background:#e3e3e3;border:none;width:120px;display:inline-block;vertical-align:top}
.subscribe{display:inline-flex;width:64px;height:22px;background:var(--ink);color:var(--white);font-size:8px;font-weight:700;align-items:center;justify-content:center;margin-left:4px}
.details{font-size:9px;color:var(--muted);line-height:1.7}
.details .row{display:flex;align-items:center;gap:6px}
.contact-right{position:absolute;left:392px;top:22px;width:638px}
.input.wide{width:100%}
.input.msg{height:76px}
.captcha{display:flex;align-items:center;gap:8px;margin-top:4px}
.captcha-code{width:50px;height:22px;background:var(--red);color:var(--white);font-size:9px;font-weight:700;display:flex;align-items:center;justify-content:center;letter-spacing:2px}
.captcha .input{width:70px;margin:0}
.submit-dark{position:absolute;right:0;bottom:-34px;width:110px;height:24px;background:var(--black);color:var(--white);font-size:9px;font-weight:700;display:flex;align-items:center;justify-content:center;letter-spacing:1px}

/* footer */
.site-footer{height:252px;background:var(--black);color:#aaa}
.footer-brand{position:absolute;left:176px;top:28px;display:flex;align-items:center;gap:10px}
.footer-brand .brand-name{color:var(--white)}
.footer-tag{position:absolute;left:176px;top:62px;font-size:10px;color:#aaa}
.social{position:absolute;left:776px;top:36px;display:flex;gap:10px}
.social span{width:24px;height:24px;border-radius:50%;background:#3a3a3a}
.credit{position:absolute;left:560px;top:106px;font-size:9px}
.copyright{position:absolute;left:176px;top:106px;font-size:9px}
</style>
</head>
<body>
<div class="page">

<header class="site-header">
  <div class="brand">
    <span class="brand-mark"></span>
    <span class="brand-name">CrashPals</span>
  </div>
  <div class="brand-tag">Personal Injury Lawyers</div>
  <div class="ebook-btn">ORDER EBOOK NOW</div>
  <nav class="main-nav">
    <a href="#">HOME</a>
    <a href="#">CLIENT RESOURCES</a>
    <a href="#">EXPERTISE / CAR WRECKS</a>
    <a href="#">CONTACT US</a>
    <a href="#">NEWS</a>
    <span class="search-btn"><svg width="12" height="12" viewBox="0 0 12 12"><circle cx="5" cy="5" r="3.5" fill="none" stroke="#fff" stroke-width="1.6"/><line x1="7.6" y1="7.6" x2="11" y2="11" stroke="#fff" stroke-width="1.6"/></svg></span>
  </nav>
</header>

<section class="hero">
  <div class="hero-media" role="img" aria-label="Photo of a crashed blue car beside a damaged white car on a road"></div>
  <div class="hero-caption">CRASHPALS ARE PERSONAL INJURY LAWYERS<br>REPRESENTING VICTIMS IN <em>ONLY CAR WRECKS</em></div>
</section>

<section class="about">
  <h2 class="section-title">ABOUT CRASHPALS</h2>
  <div class="section-rule"></div>
  <p class="section-lead">We stand only with people hurt in car wrecks. We handle claims, insurers and investigations so you can rest and heal. One focus, one promise, and full attention to every client we serve.</p>
</section>

<section class="evaluation">
  <div class="slide" role="img" aria-label="Photo of rescuers at a wrecked red car"></div>
  <div class="slide-dots"><span></span><span></span></div>
  <form class="eval-form">
    <h3>FREE CASE EVALUATION</h3>
    <div class="field">Name</div>
    <div class="field">Email</div>
    <div class="field">Contact No.</div>
    <div class="field tall">Message</div>
    <span class="btn-red">SUBMIT</span>
  </form>
</section>

<section class="team">
  <h2 class="section-title">LAWYERS TEAM</h2>
  <div class="section-rule"></div>
  <p class="section-lead">Meet the team who stands with victims of car wrecks.</p>
  <div class="team-arrows">
    <span><svg width="6" height="8" viewBox="0 0 6 8"><path d="M5 0L1 4l4 4" fill="none" stroke="#fff" stroke-width="1.5"/></svg></span>
    <span><svg width="6" height="8" viewBox="0 0 6 8"><path d="M1 0l4 4-4 4" fill="none" stroke="#fff" stroke-width="1.5"/></svg></span>
  </div>
  <div class="team-grid">
    <div class="lawyer"><div class="lawyer-photo" role="img" aria-label="Portrait photo of attorney Owen Hartley"></div><div class="lawyer-name">Owen Hartley</div><div class="lawyer-role">Partner</div><div class="lawyer-meta">Car wreck claims</div><div class="lawyer-link">Read More</div></div>
    <div class="lawyer"><div class="lawyer-photo" role="img" aria-label="Portrait photo of attorney Nadia Kerrow"></div><div class="lawyer-name">Nadia Kerrow</div><div class="lawyer-role">Partner</div><div class="lawyer-meta">Car wreck claims</div><div class="lawyer-link">Read More</div></div>
    <div class="lawyer"><div class="lawyer-photo" role="img" aria-label="Portrait photo of attorney Felix Marlow"></div><div class="lawyer-name">Felix Marlow</div><div class="lawyer-role">Attorney</div><div class="lawyer-meta">Car wreck claims</div><div class="lawyer-link">Read More</div></div>
    <div class="lawyer"><div class="lawyer-photo" role="img" aria-label="Portrait photo of attorney Clara Vennet"></div><div class="lawyer-name">Clara Vennet</div><div class="lawyer-role">Attorney</div><div class="lawyer-meta">Car wreck claims</div><div class="lawyer-link">Read More</div></div>
    <div class="lawyer"><div class="lawyer-photo" role="img" aria-label="Portrait photo of attorney Miles Ardent"></div><div class="lawyer-name">Miles Ardent</div><div class="lawyer-role">Attorney</div><div class="lawyer-meta">Car wreck claims</div><div class="lawyer-link">Read More</div></div>
    <div class="lawyer"><div class="lawyer-photo" role="img" aria-label="Portrait photo of attorney Jonah Pellam"></div><div class="lawyer-name">Jonah Pellam</div><div class="lawyer-role">Attorney</div><div class="lawyer-meta">Car wreck claims</div><div class="lawyer-link">Read More</div></div>
  </div>
</section>

<section class="video-band">
  <div class="video" role="img" aria-label="Video still of a city street seen from a car dashboard">
    <span class="video-title">Car Wrecks</span>
    <svg class="play" width="60" height="42" viewBox="0 0 60 42"><rect width="60" height="42" rx="10" fill="#ec1f27"/><path d="M24 12l14 9-14 9z" fill="#fff"/></svg>
    <div class="video-bar"><i></i></div>
  </div>
  <div class="video-copy">
    <h3>Car Wrecks</h3>
    <p>See how we guide clients through every step after a crash, from the first call to the final settlement of their claim.</p>
    <span class="btn-red">VIEW NOW</span>
  </div>
</section>

<section class="blog">
  <h2 class="section-title">LATEST FROM THE BLOG</h2>
  <div class="section-rule"></div>
  <p class="section-lead">Stories, guides and case news for people hurt in car wrecks, written by our team to help you understand your rights after a crash.</p>
  <div class="blog-grid">
    <article class="post"><div class="post-image" role="img" aria-label="Photo of people beside a crashed car" style="background:linear-gradient(135deg,#4a5a6a,#8e98a2 50%,#2f3a44)"></div><h4>WHAT TO DO IN THE FIRST HOUR AFTER A CAR WRECK</h4><div class="meta">June 12, 2015 / 3 Comments</div><p>Simple steps to keep you safe and protect your claim right after a crash on the road.</p></article>
    <article class="post"><div class="post-image" role="img" aria-label="Photo of a damaged red car on a street" style="background:linear-gradient(135deg,#2c3e6e,#a3262b 55%,#6a6f75)"></div><h4>HOW INSURERS VALUE YOUR CAR WRECK CLAIM</h4><div class="meta">June 08, 2015 / 5 Comments</div><p>A plain guide to damages, fault and the numbers insurers use when they make an offer.</p></article>
    <article class="post"><div class="post-image" role="img" aria-label="Photo of a crashed motorbike on a wet road" style="background:linear-gradient(135deg,#8fa3b0,#5d7463 55%,#3b4a3f)"></div><h4>WHY A CRASH INVESTIGATION MATTERS TO YOU</h4><div class="meta">June 02, 2015 / 2 Comments</div><p>How photos, witnesses and reports build a strong case for victims of car wrecks.</p></article>
  </div>
</section>

<section class="touch">
  <h2 class="section-title">GET IN TOUCH WITH US</h2>
  <div class="section-rule"></div>
  <p class="section-lead">Call, write or visit us. We reply fast and your first case review is always free.</p>
</section>

<section class="map" role="img" aria-label="Dark street map showing the office location">
  <div class="map-zoom"><span>+</span><span>−</span></div>
  <svg class="pin" width="20" height="28" viewBox="0 0 20 28"><path d="M10 0C4.5 0 0 4.4 0 9.8 0 17 10 28 10 28s10-11 10-18.2C20 4.4 15.5 0 10 0z" fill="#ec1f27"/><circle cx="10" cy="10" r="3.5" fill="#fff"/></svg>
</section>

<section class="contact">
  <div class="contact-left">
    <h5>NEWSLETTER</h5>
    <label>Subscribe to our Newsletter</label>
    <div><span class="input grey"></span><span class="subscribe">SUBSCRIBE</span></div>
    <h5 style="margin-top:22px">CONTACT DETAILS</h5>
    <div class="details">
      <div>1200 Example Road, Suite 5</div>
      <div>Springfield, ST 00000</div>
      <div class="row" style="margin-top:8px"><svg width="8" height="8" viewBox="0 0 8 8"><rect width="8" height="8" fill="#ec1f27"/></svg>(555) 010-0142</div>
      <div class="row"><svg width="8" height="8" viewBox="0 0 8 8"><rect width="8" height="8" fill="#ec1f27"/></svg>(555) 010-0187</div>
      <div class="row"><svg width="8" height="8" viewBox="0 0 8 8"><rect width="8" height="8" fill="#ec1f27"/></svg>info@crashpals-example.com</div>
      <div class="row"><svg width="8" height="8" viewBox="0 0 8 8"><rect width="8" height="8" fill="#ec1f27"/></svg>www.crashpals-example.com</div>
    </div>
  </div>
  <form class="contact-right">
    <h5>CONTACT FORM</h5>
    <label>Name and Surname*</label>
    <div class="input wide" style="width:320px"></div>
    <label>Email*</label>
    <div class="input wide" style="width:320px"></div>
    <label>Message*</label>
    <div class="input wide msg"></div>
    <div class="captcha"><span class="captcha-code">4X7Q</span><span class="input"></span></div>
    <span class="submit-dark">SUBMIT</span>
  </form>
</section>

<footer class="site-footer">
  <div class="footer-brand">
    <span class="brand-mark"></span>
    <span class="brand-name">CrashPals</span>
  </div>
  <div class="footer-tag">Personal Injury Lawyers</div>
  <div class="social"><span></span><span></span><span></span><span></span></div>
  <div class="copyright">Copyright © CrashPals. All rights reserved.</div>
  <div class="credit">Designed by the CrashPals team</div>
</footer>

</div>
</body>
</html>
```